Design Our Holiday Magic Coupon

Purpose - The purpose of this project is to create a festive, uplifting, and visually engaging physical coupon that will be mailed to our existing community and warm leads.
The intent is twofold: first, to spark delight and connection by offering a tangible, personal touch during the holiday season; and second, to encourage customers to explore and purchase our programs as they prepare for a strong start to 2026. This mailer is designed to re-engage past buyers, inspire current participants, and gently invite new momentum into their practice through a simple, friendly offer.

Project Description + Scope

This project includes the design and production of a printed coupon ( card format) featuring a 20% discount on purchases of $79 or more. The copy should feel warm, clear, and celebratory without urgency or pressure.

The front of the card will include the headline (“Live Your Best 2026”), bold discount information, and the coupon code FESTIVE20. The back will include a short message reinforcing the tone of possibility and ease, plus simple redemption instructions and the expiry date: December 31, 2025. Deliverables include print-ready artwork, color selection aligned with KH brand style.

one side
LIVE YOUR BEST 2026
Enjoy 20% OFF when you buy $79 or more.
Use code: FESTIVE20
Redeem until end of day December 31, 2025.

Back side - Move with clarity.
Heal with intelligence.
Lead with ease.
Thank you for being part of Kinetic Harmony.
Lots of love, Mara and the whole of Team Mara

Target Market(s)

yoga teachers, yoga lovers, mostly over 50 years, women

Font styles to use
Other font styles liked:
• see attached for feel

Colors
0054AA
0677BA
7BADD7
CADEEF
E8F1F8
0094D4
00A9DD
6FCCEA
C7EBF8
E9F6FB
00AB8E
00BBA5
67D7C9
C6EFE9
E9F9F6
EB3D1F
EC4F4E
F09395
F8D3D4
FCEDEE

Requirements
Nice to have
• see attached

```html
<!DOCTYPE html>
<html lang="en">
<head>
<meta charset="utf-8">
<title>Kinetic Harmony – Holiday Coupon</title>
<link rel="stylesheet" href="https://fonts.googleapis.com/css2?family=Montserrat:ital,wght@0,300;0,400;0,500;0,700;0,800;1,700;1,800&display=swap">
<style>
  :root {
    --page: #ffffff;
    --brand-deep: #0054AA;
    --card-top: #2f72b8;
    --card-mid: #5b96cd;
    --card-bottom: #86b4dc;
    --ink-light: #ffffff;
  }
  * { margin: 0; padding: 0; box-sizing: border-box; }
  html, body {
    width: 1200px;
    height: 953px;
    overflow: hidden;
    background: var(--page);
  }
  .sheet {
    position: relative;
    width: 1200px;
    height: 953px;
    font-family: 'Montserrat', sans-serif;
  }
  .card {
    position: absolute;
    top: 45px;
    width: 522px;
    height: 864px;
    display: block;
  }
  .card--front { left: 56px; }
  .card--back { left: 621px; }

  .card text { fill: var(--ink-light); font-family: 'Montserrat', sans-serif; }
  .brand-name { font-weight: 300; font-size: 40px; }
  .brand-dot { fill: var(--ink-light); }
  .headline { font-weight: 800; font-size: 73px; }
  .tag-box { fill: var(--brand-deep); }
  .tag-rule { stroke: var(--brand-deep); stroke-width: 3; }
  .tag-text { font-weight: 800; font-size: 49px; }
  .offer { font-weight: 700; font-size: 182px; letter-spacing: -4px; }
  .condition { font-weight: 400; font-size: 20px; }
  .condition .strong { font-weight: 800; }
  .code-text { font-weight: 400; font-size: 25px; }
  .code-text .strong { font-weight: 800; }
  .expiry { font-weight: 400; font-size: 17.5px; }
  .expiry .strong { font-weight: 700; }
  .grid-line { stroke: var(--ink-light); stroke-width: 1.5; }
  .mantra { font-weight: 400; font-size: 30px; }
  .mantra .em { font-weight: 800; font-style: italic; }
  .thanks { font-weight: 400; font-size: 16.5px; }
  .signoff { font-weight: 400; font-size: 26px; }
  .signoff .strong { font-weight: 800; }
  .closing-rule { stroke: var(--ink-light); stroke-width: 2; }
</style>
</head>
<body>
<main class="sheet">

  <!-- Front: offer -->
  <svg class="card card--front" viewBox="0 0 522 864" aria-label="Kinetic Harmony holiday coupon, front">
    <defs>
      <linearGradient id="front-bg" x1="1" y1="0" x2="0" y2="1">
        <stop offset="0" stop-color="var(--card-top)"/>
        <stop offset="0.55" stop-color="var(--card-mid)"/>
        <stop offset="1" stop-color="var(--card-bottom)"/>
      </linearGradient>
    </defs>
    <rect width="522" height="864" fill="url(#front-bg)"/>

    <g class="brand" aria-label="Kinetic Harmony">
      <circle class="brand-dot" cx="174" cy="85" r="40"/>
      <text class="brand-name" x="238" y="86">kinetic</text>
      <text class="brand-name" x="238" y="117">harmony</text>
    </g>

    <text class="headline" x="261" y="222" text-anchor="middle" textLength="393" lengthAdjust="spacingAndGlyphs">LIVE YOUR</text>
    <text class="headline" x="261" y="296" text-anchor="middle" textLength="382" lengthAdjust="spacingAndGlyphs">BEST 2026</text>

    <line class="tag-rule" x1="0" y1="356" x2="522" y2="356"/>
    <rect class="tag-box" x="163" y="327" width="197" height="58"/>
    <text class="tag-text" x="261.5" y="374" text-anchor="middle" textLength="156" lengthAdjust="spacingAndGlyphs">ENJOY</text>

    <text class="offer" x="261" y="539" text-anchor="middle" textLength="367" lengthAdjust="spacingAndGlyphs">20%</text>
    <text class="offer" x="261" y="697" text-anchor="middle" textLength="370" lengthAdjust="spacingAndGlyphs">OFF</text>

    <text class="condition" x="261" y="739" text-anchor="middle" textLength="329" lengthAdjust="spacingAndGlyphs">WHEN YOU <tspan class="strong">BUY $79 OR MORE</tspan></text>

    <rect class="tag-box" x="110" y="766" width="303" height="42" rx="9"/>
    <text class="code-text" x="261.5" y="796" text-anchor="middle" textLength="284" lengthAdjust="spacingAndGlyphs">USE CODE: <tspan class="strong">FESTIVE20</tspan></text>

    <text class="expiry" x="261" y="846" text-anchor="middle" textLength="405" lengthAdjust="spacingAndGlyphs">Redeem until end of day <tspan class="strong">December 31, 2025.</tspan></text>
  </svg>

  <!-- Back: message -->
  <svg class="card card--back" viewBox="0 0 522 864" aria-label="Kinetic Harmony holiday coupon, back">
    <defs>
      <linearGradient id="back-bg" x1="1" y1="0" x2="0" y2="1">
        <stop offset="0" stop-color="var(--card-top)"/>
        <stop offset="0.55" stop-color="var(--card-mid)"/>
        <stop offset="1" stop-color="var(--card-bottom)"/>
      </linearGradient>
    </defs>
    <rect width="522" height="864" fill="url(#back-bg)"/>

    <g class="brand" aria-label="Kinetic Harmony">
      <circle class="brand-dot" cx="174" cy="125" r="40"/>
      <text class="brand-name" x="238" y="125">kinetic</text>
      <text class="brand-name" x="238" y="156">harmony</text>
    </g>

    <g class="mantra-grid">
      <line class="grid-line" x1="57" y1="236" x2="57" y2="501"/>
      <line class="grid-line" x1="463" y1="236" x2="463" y2="501"/>
      <line class="grid-line" x1="42" y1="260" x2="478" y2="260"/>
      <line class="grid-line" x1="42" y1="329" x2="478" y2="329"/>
      <line class="grid-line" x1="42" y1="403" x2="478" y2="403"/>
      <line class="grid-line" x1="42" y1="479" x2="478" y2="479"/>
    </g>
    <text class="mantra" x="261" y="306" text-anchor="middle" textLength="283" lengthAdjust="spacingAndGlyphs">Move with <tspan class="em">clarity.</tspan></text>
    <text class="mantra" x="261" y="381" text-anchor="middle" textLength="364" lengthAdjust="spacingAndGlyphs">Heal with <tspan class="em">Intelligence.</tspan></text>
    <text class="mantra" x="261" y="451" text-anchor="middle" textLength="265" lengthAdjust="spacingAndGlyphs"><tspan class="em">Lead</tspan> With <tspan class="em">Ease.</tspan></text>

    <text class="thanks" x="261" y="550" text-anchor="middle">THANK YOU FOR</text>
    <text class="thanks" x="261" y="579" text-anchor="middle" textLength="370" lengthAdjust="spacingAndGlyphs">BEING PART OF KINETIC HARMONY.</text>

    <text class="signoff" x="261" y="634" text-anchor="middle"><tspan class="strong">LOTS OF LOVE,</tspan></text>
    <text class="signoff" x="261" y="667" text-anchor="middle"><tspan class="strong">MARA</tspan> AND THE WHOLE</text>
    <text class="signoff" x="261" y="701" text-anchor="middle">OF <tspan class="strong">TEAM MARA</tspan></text>

    <line class="closing-rule" x1="207" y1="814" x2="315" y2="814"/>
  </svg>

</main>
</body>
</html>
```